Website/Logo redesign: FieldKinship.com

We need a web design for a sports social network.
We have already built the web-site but are unhappy with the current design.
We like colours that evoke outdoors, eg sky blue and grass green.
Please see how it currently looks:
http://www.fieldkinship.example/4b1a9c3e7d2f5a8b0c6e1f3a9d7b2c5e/
We are happy for everything to change, including logo, icons etc or for you to keep anything you think will work with your new design.
Reason: We have not yet found the design we are happy with so will be providing more feedback and extending the deadine.
We have increased the budget and also agreed to pay a second place award.
I will be giving existing and any new designs feedback daily.
Target Market(s)
Our target audience are mainly young sports players, but also older ones too.
Industry/Entity Type
Social
Look and feel

```html
<!DOCTYPE html>
<html lang="en">
<head>
<meta charset="utf-8">
<title>Field Kinship – Headlines</title>
<link href="https://fonts.googleapis.com/css2?family=Tinos&family=Oswald:wght@400;500&family=Arimo:wght@400;700&family=Gelasio:ital@0;1&display=swap" rel="stylesheet">
<style>
:root{
  --black:#000;
  --nav-green:#8cc63f;
  --nav-active:#4d6b25;
  --nav-border:#5c8a22;
  --panel:rgba(245,248,240,.72);
  --panel-strong:rgba(250,251,248,.9);
  --line:rgba(120,130,110,.35);
  --text:#3a3a3a;
  --muted:#8a8f86;
  --team-green:#3a9a1e;
  --team-red:#d9501c;
  --badge:#d8262d;
  --white:#fff;
}
*{box-sizing:border-box;margin:0;padding:0}
html,body{width:1050px;height:1200px;overflow:hidden;background:var(--black)}
body{position:relative;font-family:"Arimo",Arial,sans-serif;color:var(--text);font-size:10px}
.abs{position:absolute}
.grass{left:0;top:128px;width:1050px;height:1032px;background:linear-gradient(180deg,#b6dc84 0%,#8fc452 30%,#6aa735 60%,#3f7415 85%,#2c5410 100%)}
.topbar{left:0;top:0;width:1050px;height:46px;background:var(--black);color:var(--white);font-family:"Tinos",serif;font-size:20px}
.topbar .welcome{position:absolute;left:22px;top:12px}
.topbar .login{position:absolute;left:942px;top:12px}
.nav{left:0;top:46px;width:1050px;height:82px;background:linear-gradient(180deg,#9bd150,#82bc38);border-bottom:2px solid var(--nav-border)}
.brand{position:absolute;left:50px;top:13px;display:flex;align-items:center;gap:6px}
.brand-mark{width:53px;height:53px;background:var(--white);border:1px solid #cfe3b0}
.brand-name{font-family:"Oswald",sans-serif;font-size:25px;color:var(--white);letter-spacing:.5px;font-weight:500;white-space:nowrap}
.tabs{position:absolute;left:439px;top:0;display:flex;height:80px}
.tab{width:73.5px;height:80px;border-left:1px solid var(--nav-border);position:relative;color:#34521a;font-family:"Oswald",sans-serif;font-size:11px;text-align:center}
.tab svg{position:absolute;left:24px;top:16px;width:26px;height:26px}
.tab span{position:absolute;left:0;right:0;top:52px}
.tab.active{background:var(--nav-active);color:var(--white)}
.tab .badge{position:absolute;left:44px;top:8px;width:20px;height:20px;border-radius:50%;background:var(--badge);color:var(--white);font-family:"Arimo",sans-serif;font-size:11px;font-weight:700;line-height:20px}
.signup{position:absolute;left:953px;top:8px;width:97px;height:72px;border-left:1px solid var(--nav-border);color:var(--white);font-family:"Tinos",serif;font-size:20px;line-height:24px;text-align:center;padding-top:4px}
.hero-stadium{left:21px;top:128px;width:524px;height:160px;background:linear-gradient(180deg,#4a6fa0 0%,#8fb0d6 35%,#2d3a4a 55%,#3f8a25 72%,#5aaa30 100%)}
.hero-player{left:545px;top:128px;width:488px;height:160px;background:linear-gradient(90deg,#5a2a22 0%,#8a4a35 40%,#6a6a60 70%,#3f8a30 100%)}
.col-left{left:21px;top:288px;width:323px;height:844px;background:var(--panel)}
.col-center{left:344px;top:288px;width:402px;height:743px;background:var(--panel-strong)}
.col-right{left:746px;top:288px;width:287px;height:844px;background:var(--panel)}
.bottombar{left:0;top:1160px;width:1050px;height:40px;background:var(--black)}
.heading{font-weight:700;font-size:10px;letter-spacing:.4px;color:#4a4a4a;text-transform:uppercase;white-space:nowrap}
.heading.light{color:#8a9080;font-size:12px}
.box{border:1px solid var(--line);background:rgba(255,255,255,.25)}
.avatar{background:linear-gradient(160deg,#d8b48a,#8a6a4a)}
.profile{left:120px;top:291px;width:196px;height:113px}
.profile .avatar{left:10px;top:6px;width:48px;height:48px}
.profile .name{left:72px;top:12px;font-weight:700;font-size:12px;white-space:nowrap}
.pill{border:1px solid #c6cbbf;border-radius:9px;background:#f3f4f0;color:#777;font-size:10px;text-align:center;white-space:nowrap}
.profile .edit{left:72px;top:32px;width:72px;height:18px;line-height:16px}
.profile .rule{left:0;top:62px;width:194px;border-top:1px solid var(--line)}
.stat{top:74px;width:60px;color:var(--muted);font-size:10px}
.stat b{display:block;font-size:15px;color:#555;font-weight:700;margin-bottom:2px}
.create{left:120px;top:431px;width:196px;height:34px;line-height:32px;padding-left:40px;font-size:11px;font-weight:700;letter-spacing:.5px;color:#555;white-space:nowrap}
.create::before{content:"+";position:absolute;left:12px;top:0;font-size:20px;color:#555}
.teams-head{left:121px;top:514px;width:222px;height:37px;border-top:1px solid var(--line);border-bottom:1px solid var(--line);padding:14px 0 0 38px}
.team-row{left:42px;width:301px;height:36px;border-bottom:1px solid var(--line);color:#aab0a4;font-size:10px;padding:12px 0 0 116px;letter-spacing:.5px;white-space:nowrap}
.team-row svg{position:absolute;left:88px;top:11px}
.quote-head{left:132px;top:706px;width:211px;border-bottom:1px solid var(--line);padding-bottom:12px}
.quote{left:132px;top:741px;width:180px;font-family:"Gelasio",serif;font-size:12px;line-height:18px;color:#7a7f74}
.quote .by{display:block;text-align:right;font-style:italic;margin-top:2px}
.ico{width:34px;height:34px;border:1px solid #c9cdc2;background:#f6f6f2;border-radius:2px}
.ico-round{width:22px;height:22px;border-radius:50%;border:1px solid #c9cdc2;background:#f4f5f0}
.ico svg,.ico-round svg{display:block;margin:auto}
.g{color:var(--team-green);font-weight:700}
.r{color:var(--team-red);font-weight:700}
.date{color:#666;font-size:9.5px;white-space:nowrap}
.rsvp{font-weight:700;font-size:9.5px;color:#444;white-space:nowrap}
.btn-on{border-radius:9px;background:linear-gradient(#8fd04a,#5aa81e);color:var(--white);font-size:9.5px;text-align:center;height:18px;line-height:18px}
.divider{border-top:1px solid var(--line)}
.mini{height:18px;border:1px solid #c9cdc2;border-radius:9px;background:#f3f4f0}
.comment{width:330px;height:50px}
.comment .avatar{width:35px;height:35px}
.comment .who{font-weight:700;font-size:9.5px;color:#333;white-space:nowrap}
.comment .msg{color:#888;font-size:9.5px;line-height:12px;width:218px}
.ago{color:#888;font-size:9.5px;white-space:nowrap}
.input{border:1px solid #d3d6cd;background:#fff;border-radius:2px;color:#c0c0c0;font-size:9.5px;padding:5px 8px;white-space:nowrap}
.score{width:26px;height:20px;border:1px solid #c9cdc2;background:#f3f4f0;font-size:13px;font-weight:700;text-align:center;line-height:19px;color:#444}
.feed{width:370px;height:60px}
.feed .avatar{width:36px;height:36px}
.feed .line{font-size:9.5px;color:#555;line-height:12px}
.check{width:20px;height:20px;border-radius:50%;border:1px solid #c9cdc2;background:#eee}
.check.on{background:linear-gradient(#8fd04a,#5aa81e);border-color:#5aa81e}
.league{left:766px;top:609px;width:246px;height:221px}
.league .title{height:32px;border-bottom:1px solid var(--line);font-weight:700;color:#777;font-size:11px;text-align:center;line-height:32px;white-space:nowrap}
.league table{width:100%;border-collapse:collapse;margin-top:16px;font-size:10px;color:#666;font-weight:700}
.league td{height:31.5px;border-bottom:1px solid var(--line)}
.league td.n{width:38px;text-align:center}
.league td.p{width:40px;text-align:right;padding-right:10px}
.league td.pts{width:40px;text-align:right;padding-right:12px}
.league .mark{border:1px solid #c9cdc2;border-radius:9px;padding:2px 6px;background:#f3f4f0}
</style>
</head>
<body>
<div class="abs grass" role="img" aria-label="Close-up photograph of fresh green grass filling the page background"></div>

<header class="abs topbar">
  <span class="welcome">WELCOME TO THE FIELD KINSHIP'S OFFICIAL WEBSITE.</span>
  <span class="login">LOG IN</span>
</header>

<nav class="abs nav">
  <div class="brand"><div class="brand-mark"></div><span class="brand-name">FIELD KINSHIP</span></div>
  <div class="tabs">
    <div class="tab active"><svg viewBox="0 0 26 26"><path d="M6 3v21" stroke="#fff" stroke-width="2"/><path d="M7 4h14l-4 5 4 5H7z" fill="#fff"/></svg><div class="badge">2</div><span>HEADLINES</span></div>
    <div class="tab"><svg viewBox="0 0 26 26" fill="none" stroke="#34521a" stroke-width="1.5"><path d="M3 3v20h20"/><path d="M5 20l5-7 4 3 8-11"/></svg><span>MY STATS</span></div>
    <div class="tab"><svg viewBox="0 0 26 26"><path d="M13 2c2 5 7 7 7 14a7 7 0 0 1-14 0c0-4 3-6 3-9 2 2 2 4 2 5 2-3 3-6 2-10z" fill="#34521a"/></svg><div class="badge">1</div><span>CHLLNGRS</span></div>
    <div class="tab"><svg viewBox="0 0 26 26" fill="none" stroke="#34521a" stroke-width="1.5"><rect x="4" y="5" width="18" height="18"/><path d="M4 10h18M8 3v4M18 3v4M8 14h2M12 14h2M16 14h2M8 18h2M12 18h2M16 18h2"/></svg><span>FIXTURES</span></div>
    <div class="tab"><svg viewBox="0 0 26 26" fill="#34521a"><circle cx="8" cy="9" r="3"/><circle cx="18" cy="9" r="3"/><circle cx="13" cy="8" r="3.5"/><path d="M2 20c0-4 3-6 6-6s6 2 6 6zM12 20c0-4 3-6 6-6s6 2 6 6z"/><path d="M7 21c0-5 3-8 6-8s6 3 6 8z"/></svg><span>TEAMS</span></div>
    <div class="tab"><svg viewBox="0 0 26 26" fill="none" stroke="#34521a" stroke-width="1.5"><rect x="5" y="3" width="16" height="20"/><path d="M5 8h16M5 13h16M5 18h16M10 3v20"/></svg><span>LEAGUES</span></div>
    <div class="tab"><svg viewBox="0 0 26 26" fill="none" stroke="#34521a" stroke-width="2.2" stroke-linecap="round"><path d="M5 21L16 10M14 6a4 4 0 0 1 6 6M6 5l4 4M21 21l-6-6"/></svg><span>TOOLS</span></div>
  </div>
  <div class="signup">OR<br>SIGN UP</div>
</nav>

<div class="abs hero-stadium" role="img" aria-label="Photograph of a floodlit football stadium with a leather ball resting on the pitch"></div>
<div class="abs hero-player" role="img" aria-label="Photograph of a footballer in a white kit striking the ball in front of a crowd"></div>

<main>
  <div class="abs col-left"></div>
  <div class="abs col-center"></div>
  <div class="abs col-right"></div>

  <section class="abs box profile">
    <div class="abs avatar" role="img" aria-label="Profile photo of Tom Ridley"></div>
    <div class="abs name">Tom Ridley</div>
    <div class="abs pill edit">Edit profile</div>
    <div class="abs rule"></div>
    <div class="abs stat" style="left:10px"><b>24</b>Played</div>
    <div class="abs stat" style="left:78px"><b>3</b>Teams</div>
    <div class="abs stat" style="left:146px"><b>7</b>Awards</div>
  </section>

  <div class="abs box create">CREATE NEW FIXTURE</div>

  <div class="abs teams-head heading">All Teams</div>
  <div class="abs team-row" style="top:551px"><svg width="14" height="14" viewBox="0 0 14 14"><circle cx="7" cy="7" r="6" fill="none" stroke="#aab0a4"/><path d="M7 4l3 2-1 3H5L4 6z" fill="#aab0a4"/></svg>U15 FOOTBALL TEAM B</div>
  <div class="abs team-row" style="top:587px"><svg width="14" height="14" viewBox="0 0 14 14"><circle cx="7" cy="7" r="6" fill="none" stroke="#aab0a4"/><path d="M7 4l3 2-1 3H5L4 6z" fill="#aab0a4"/></svg>GALATIANS HOUSE</div>
  <div class="abs team-row" style="top:623px"><svg width="14" height="14" viewBox="0 0 14 14"><circle cx="7" cy="7" r="6" fill="none" stroke="#aab0a4"/><path d="M7 4l3 2-1 3H5L4 6z" fill="#aab0a4"/></svg>U15 RUGBY TEAM A</div>

  <div class="abs quote-head heading">Quote of the day</div>
  <p class="abs quote">Champions aren’t made in the gyms. Champions are made from something they have deep inside them — a desire, a dream, a vision.<span class="by">— Marcus Alden</span></p>

  <!-- Next fixture -->
  <div class="abs heading" style="left:365px;top:305px">Next Fixture</div>
  <div class="abs ico" style="left:366px;top:330px"><svg width="26" height="26" viewBox="0 0 26 26" style="margin-top:3px"><circle cx="13" cy="13" r="11" fill="#fff" stroke="#333"/><path d="M13 8l4 3-1.5 5h-5L9 11z" fill="#333"/></svg></div>
  <div class="abs ico-round" style="left:414px;top:336px"><svg width="14" height="14" viewBox="0 0 14 14" style="margin-top:3px"><rect x="1" y="7" width="4" height="5" fill="#777"/><rect x="5" y="4" width="4" height="8" fill="#555"/><rect x="9" y="8" width="4" height="4" fill="#777"/></svg></div>
  <div class="abs" style="left:449px;top:334px;font-size:9.5px;white-space:nowrap"><span class="g">U15 Football Team</span> vs <span class="r">Colossians House</span></div>
  <div class="abs date" style="left:449px;top:348px">Sunday, 29th July, 1 PM</div>
  <div class="abs rsvp" style="left:449px;top:370px">RSVP:</div>
  <div class="abs btn-on" style="left:492px;top:366px;width:62px">Available</div>
  <div class="abs pill" style="left:558px;top:366px;width:78px;height:18px;line-height:16px">Unavailable</div>
  <div class="abs divider" style="left:366px;top:407px;width:252px"></div>
  <div class="abs mini" style="left:619px;top:398px;width:42px"></div>
  <div class="abs mini" style="left:668px;top:398px;width:42px"></div>
  <div class="abs divider" style="left:711px;top:407px;width:14px"></div>

  <div class="abs comment" style="left:401px;top:424px">
    <div class="abs avatar" role="img" aria-label="Profile photo of Mr. Hallworth" style="left:0;top:0"></div>
    <div class="abs who" style="left:48px;top:0">Mr. Hallworth</div>
    <div class="abs msg" style="left:48px;top:12px">Don’t be late minibus will be leaving at 11:30 AM on the dot, anybody late will miss it!</div>
    <div class="abs ago" style="left:280px;top:24px">2m ago</div>
  </div>
  <div class="abs comment" style="left:401px;top:474px">
    <div class="abs avatar" role="img" aria-label="Profile photo of Sina Spalding" style="left:0;top:0"></div>
    <div class="abs who" style="left:48px;top:0">Sina Spalding</div>
    <div class="abs msg" style="left:48px;top:12px">Remember last time we played this lot, they had that really good center forward, whoever is marking him, stay tight to him</div>
    <div class="abs ago" style="left:283px;top:36px">1h ago</div>
  </div>
  <div class="abs comment" style="left:401px;top:537px">
    <div class="abs avatar" role="img" aria-label="Profile photo of Jana Abel" style="left:0;top:0"></div>
    <div class="abs who" style="left:48px;top:0">Jana Abel</div>
    <div class="abs msg" style="left:48px;top:12px">Yeah and also quick passes as this lot will close you down really quick</div>
    <div class="abs ago" style="left:282px;top:24px">6h ago</div>
  </div>
  <div class="abs input" style="left:449px;top:592px;width:182px;height:22px">Leave your comment here</div>
  <div class="abs pill" style="left:642px;top:592px;width:68px;height:22px;line-height:20px;color:#555">Submit</div>
  <div class="abs divider" style="left:366px;top:636px;width:358px"></div>

  <!-- Last result -->
  <div class="abs heading" style="left:365px;top:646px">Last Result</div>
  <div class="abs ico" style="left:366px;top:668px"><svg width="26" height="26" viewBox="0 0 26 26" style="margin-top:3px"><circle cx="13" cy="13" r="11" fill="#fff" stroke="#333"/><path d="M13 8l4 3-1.5 5h-5L9 11z" fill="#333"/></svg></div>
  <div class="abs ico-round" style="left:414px;top:674px"><svg width="14" height="14" viewBox="0 0 14 14" style="margin-top:3px"><rect x="1" y="7" width="4" height="5" fill="#777"/><rect x="5" y="4" width="4" height="8" fill="#555"/><rect x="9" y="8" width="4" height="4" fill="#777"/></svg></div>
  <div class="abs" style="left:449px;top:677px;font-size:9.5px;white-space:nowrap"><span class="g">Ashworth Danes</span> vs <span class="r">Hollins Park U15</span></div>
  <div class="abs date" style="left:449px;top:691px">Friday, 27th July, 1 PM</div>
  <div class="abs score" style="left:449px;top:710px">2</div>
  <div class="abs" style="left:482px;top:711px;font-weight:700;font-size:12px">:</div>
  <div class="abs score" style="left:493px;top:710px">1</div>
  <div class="abs divider" style="left:366px;top:755px;width:264px"></div>
  <div class="abs mini" style="left:631px;top:746px;width:30px"></div>
  <div class="abs mini" style="left:668px;top:746px;width:42px"></div>
  <div class="abs divider" style="left:711px;top:755px;width:14px"></div>

  <!-- News feed -->
  <div class="abs heading" style="left:365px;top:782px">News Feed</div>
  <div class="abs divider" style="left:365px;top:798px;width:360px"></div>
  <div class="abs" style="left:426px;top:820px;height:170px;border-left:1px solid #c9cdc2"></div>
  <div class="abs feed" style="left:366px;top:807px">
    <div class="abs avatar" role="img" aria-label="Profile photo of Mr. Hallworth" style="left:0;top:0"></div>
    <div class="abs ico-round" style="left:49px;top:11px"><svg width="14" height="14" viewBox="0 0 14 14" style="margin-top:3px"><rect x="1" y="7" width="4" height="5" fill="#777"/><rect x="5" y="4" width="4" height="8" fill="#555"/><rect x="9" y="8" width="4" height="4" fill="#777"/></svg></div>
    <div class="abs line" style="left:83px;top:2px;width:240px"><b>Mr. Hallworth</b> invites you to a match<br><span class="g">U15 Football Team</span> vs <span class="r">Colossians House</span><br><span class="date">Sunday, 29th July, 1 PM</span></div>
    <svg class="abs" style="left:330px;top:10px" width="14" height="14" viewBox="0 0 14 14" fill="none" stroke="#555"><rect x="1.5" y="2.5" width="11" height="10"/><path d="M1.5 5.5h11M4 8h6M4 10h6"/></svg>
    <div class="abs rsvp" style="left:83px;top:52px">RSVP:</div>
    <div class="abs check on" style="left:124px;top:48px"><svg width="12" height="12" viewBox="0 0 12 12" style="margin-top:3px"><path d="M2 6l3 3 5-6" stroke="#fff" stroke-width="2" fill="none"/></svg></div>
    <div class="abs check" style="left:150px;top:48px"><svg width="10" height="10" viewBox="0 0 10 10" style="margin-top:4px"><path d="M2 2l6 6M8 2l-6 6" stroke="#888" stroke-width="1.8"/></svg></div>
    <div class="abs ago" style="left:333px;top:53px">1h ago</div>
  </div>
  <div class="abs feed" style="left:366px;top:899px">
    <div class="abs avatar" role="img" aria-label="Profile photo of Jana Abel" style="left:0;top:0"></div>
    <div class="abs ico-round" style="left:49px;top:6px"><svg width="12" height="14" viewBox="0 0 12 14" style="margin-top:3px"><path d="M6 1c1 3 4 4 4 8a4 4 0 0 1-8 0c0-2 2-3 2-5 1 1 1 2 1 3 1-2 2-3 1-6z" fill="#555"/></svg></div>
    <div class="abs line" style="left:83px;top:2px;width:250px"><b>Jana Abel</b> has challenged you to <b>squash</b><br><span class="date">Sunday, 1st August, 1 PM, Carden Sports Centre</span></div>
    <div class="abs rsvp" style="left:83px;top:41px">RSVP:</div>
    <div class="abs check" style="left:124px;top:37px"><svg width="12" height="12" viewBox="0 0 12 12" style="margin-top:3px"><path d="M2 6l3 3 5-6" stroke="#888" stroke-width="2" fill="none"/></svg></div>
    <div class="abs check" style="left:150px;top:37px"><svg width="10" height="10" viewBox="0 0 10 10" style="margin-top:4px"><path d="M2 2l6 6M8 2l-6 6" stroke="#888" stroke-width="1.8"/></svg></div>
    <div class="abs ago" style="left:333px;top:41px">6h ago</div>
  </div>
  <div class="abs feed" style="left:366px;top:977px">
    <div class="abs avatar" role="img" aria-label="Profile photo of Josef Barlow" style="left:0;top:0;width:34px;height:34px"></div>
    <div class="abs ico-round" style="left:49px;top:6px"><svg width="12" height="12" viewBox="0 0 12 12" style="margin-top:4px"><path d="M3 1h6v3a3 3 0 0 1-6 0zM6 7v2M4 11h4" stroke="#555" fill="none" stroke-width="1.4"/></svg></div>
    <div class="abs line" style="left:83px;top:4px;width:240px"><b>Josef Barlow</b> gained an achievement<br><b>“Played 100 hours of sport”</b></div>
    <div class="abs ago" style="left:333px;top:16px">2d ago</div>
  </div>

  <!-- Upcoming fixtures -->
  <div class="abs heading light" style="left:779px;top:306px">Upcoming Fixtures</div>
  <div class="abs" style="left:791px;top:368px;height:168px;border-left:1px solid #c9cdc2"></div>
  <div class="abs ico-round" style="left:779px;top:344px"><svg width="14" height="14" viewBox="0 0 14 14" style="margin-top:3px"><rect x="1" y="7" width="4" height="5" fill="#777"/><rect x="5" y="4" width="4" height="8" fill="#555"/><rect x="9" y="8" width="4" height="4" fill="#777"/></svg></div>
  <div class="abs ico-round" style="left:779px;top:377px"><svg width="16" height="16" viewBox="0 0 16 16" style="margin-top:2px"><circle cx="8" cy="8" r="7" fill="#fff" stroke="#333"/><path d="M8 5l3 2-1 3H6L5 7z" fill="#333"/></svg></div>
  <div class="abs" style="left:824px;top:341px;font-size:11.5px;line-height:14px;width:180px"><span class="g">U15 Football Team</span> vs<br><span class="r">Colossians House</span></div>
  <div class="abs" style="left:824px;top:372px;font-size:11px;color:#555">29th July</div>
  <div class="abs rsvp" style="left:824px;top:396px;font-size:11px;color:#555">RSVP:&nbsp; Available</div>
  <div class="abs divider" style="left:746px;top:432px;width:260px"></div>
  <div class="abs ico-round" style="left:779px;top:459px"><svg width="14" height="14" viewBox="0 0 14 14" style="margin-top:3px"><rect x="1" y="7" width="4" height="5" fill="#777"/><rect x="5" y="4" width="4" height="8" fill="#555"/><rect x="9" y="8" width="4" height="4" fill="#777"/></svg></div>
  <div class="abs ico-round" style="left:779px;top:492px"><svg width="16" height="16" viewBox="0 0 16 16" style="margin-top:2px"><circle cx="8" cy="8" r="7" fill="#fff" stroke="#333"/><path d="M8 5l3 2-1 3H6L5 7z" fill="#333"/></svg></div>
  <div class="abs" style="left:824px;top:456px;font-size:11.5px;line-height:14px;width:180px"><span class="g">U15 Football Team</span> vs<br><span class="r">Romans House</span></div>
  <div class="abs" style="left:824px;top:487px;font-size:11px;color:#555">6th August</div>
  <div class="abs rsvp" style="left:824px;top:511px;font-size:11px;color:#555">RSVP:&nbsp; Available</div>
  <div class="abs divider" style="left:746px;top:548px;width:260px"></div>

  <!-- League table -->
  <div class="abs heading light" style="left:779px;top:571px">League Table</div>
  <section class="abs box league">
    <div class="title">Ashworth Inter House Football</div>
    <table>
      <tr><td class="n">1</td><td>Colossians</td><td class="p">12</td><td class="pts">36</td></tr>
      <tr><td class="n">2</td><td>Philippians</td><td class="p">12</td><td class="pts">30</td></tr>
      <tr><td class="n">3</td><td><span class="mark">Galatians</span></td><td class="p">11</td><td class="pts">12</td></tr>
      <tr><td class="n">4</td><td>Romans</td><td class="p">12</td><td class="pts">4</td></tr>
      <tr><td class="n">5</td><td>Corinthians</td><td class="p">11</td><td class="pts">1</td></tr>
    </table>
  </section>
</main>

<footer class="abs bottombar"></footer>
</body>
</html>
```